Business Card Design

Bramwell Pantry is the name of my health coaching business. My tag line is "Where good health meets real life." I will be working with clients one-on-one and in groups. My target clients are women "of a certain age" who want to be more comfortable in their own skin. We will work together in a 6-month program. The coaching sessions will take place in my kitchen. I will also be conducting monthly cooking classes and field trips - to farmer's markets, speciality markets etc.. for my clients.
Updates

the business name is Bramwell Pantry - I'm not sure how the p got in there at the end of the name

Thank you

Please include the website - www.bramwellpantry-example.com and the tag line:

Where good health meets real life on the business card.

Thank you

Please add the phone number to the business card - sorry, I forgot to state that in the original brief

(555) 218-4476

Target Market(s)

Women "of a certain age" who want to be more comfortable in their own skin

Industry/Entity Type

Cooking

Contact Information for Business Card

Bramwell Pantry
Where good health meets real life

Harriet Dunmore
Health Coach
(555) 218-4476

Font styles to use
Serif
Sans Serif

Requirements
Must have
• front & back design
I typical like soft colors - and have tended toward greens over time - I'm open although I would not like bright reds, yellows etc..

```html
<!DOCTYPE html>
<html lang="en">
<head>
<meta charset="utf-8">
<title>Bramwell Pantry – Business Card</title>
<link href="https://fonts.googleapis.com/css2?family=Open+Sans:wght@400;600&family=Patrick+Hand&display=swap" rel="stylesheet">
<style>
  :root {
    --stage: #2f2f2f;
    --card: #4a7a39;
    --card-light: #5f8f4c;
    --ink: #c9e6b2;
    --ink-dark: #3f6f2f;
    --label-bg: #c9e6b2;
  }
  * { margin: 0; padding: 0; box-sizing: border-box; }
  html, body { width: 1200px; height: 1000px; overflow: hidden; }
  body { background: var(--stage); position: relative; font-family: "Open Sans", sans-serif; color: var(--ink); }

  .card { position: absolute; left: 243px; width: 702px; height: 390px; overflow: hidden; }
  .card--front { top: 93px; }
  .card--back { top: 525px; }

  .card__pattern {
    position: absolute; inset: 0;
    background: radial-gradient(ellipse at 50% 45%, var(--card) 30%, var(--card-light) 120%);
  }

  .promise {
    position: absolute; left: 90px; top: 158px;
    font-family: "Patrick Hand", cursive; font-size: 27px; line-height: 35px; letter-spacing: 2.4px;
    white-space: nowrap;
  }

  .website { position: absolute; left: 194px; top: 304px; width: 300px; text-align: center; }
  .website svg { display: block; margin: 0 auto; }
  .website__rule { width: 200px; height: 3px; background: var(--ink); margin: 2px auto 0; }
  .website__url { font-size: 16px; letter-spacing: -0.4px; margin-top: 1px; white-space: nowrap; }

  .person__name {
    position: absolute; right: 20px; top: 32px; height: 34px; padding: 0 6px 0 26px;
    background: var(--label-bg); color: var(--ink-dark);
    font-size: 25px; font-weight: 600; line-height: 34px;
    box-shadow: 0 0 6px var(--label-bg);
  }
  .person__role { position: absolute; right: 23px; top: 64px; font-size: 26px; font-weight: 600; }

  .brand { position: absolute; left: 80px; top: 140px; white-space: nowrap; }
  .brand__primary { font-size: 64px; font-weight: 600; letter-spacing: -1.5px; }
  .brand__secondary { font-size: 40px; font-weight: 600; margin-left: 8px; }
  .tagline {
    position: absolute; left: 397px; top: 218px;
    font-family: "Patrick Hand", cursive; font-size: 21px; letter-spacing: 0.6px; white-space: nowrap;
  }

  .contact { position: absolute; top: 300px; text-align: center; }
  .contact svg { display: block; margin: 0 auto; }
  .contact__rule { height: 3px; background: var(--ink); margin-top: 2px; }
  .contact__text { margin-top: 2px; white-space: nowrap; }
  .contact--email { left: 22px; width: 196px; }
  .contact--email .contact__text { font-size: 12.5px; letter-spacing: -0.5px; margin-left: -12px; margin-right: -12px; }
  .contact--social { left: 240px; width: 214px; }
  .contact--social .contact__text { font-size: 20px; font-weight: 600; letter-spacing: 1.5px; }
  .contact--phone { left: 470px; width: 214px; }
  .contact--phone .contact__text { font-size: 19px; font-weight: 600; letter-spacing: 1.2px; }
</style>
</head>
<body>

<section class="card card--front">
  <div class="card__pattern" role="img" aria-label="Faint pattern of kitchen utensil silhouettes: teapot, cutlery, cups, pots and knives"></div>
  <p class="promise">Reach your health and weight loss goals<br>with a plan designed just for you.</p>
  <div class="website">
    <svg width="40" height="38" viewBox="0 0 40 38" fill="none" stroke="var(--ink)" stroke-width="2">
      <circle cx="16" cy="17" r="14"/>
      <ellipse cx="16" cy="17" rx="6" ry="14"/>
      <line x1="2" y1="17" x2="30" y2="17"/>
      <circle cx="25" cy="14" r="6" fill="var(--card)"/>
      <line x1="29" y1="18" x2="36" y2="26" stroke-width="3"/>
    </svg>
    <div class="website__rule"></div>
    <div class="website__url">www.bramwellpantry-example.com</div>
  </div>
</section>

<section class="card card--back">
  <div class="card__pattern" role="img" aria-label="Faint pattern of kitchen utensil silhouettes: teapot, cutlery, cups, pots and knives"></div>

  <div class="person__name">Harriet Dunmore</div>
  <div class="person__role">Health Coach</div>

  <div class="brand"><span class="brand__primary">Bramwell</span><span class="brand__secondary">Pantry</span></div>
  <p class="tagline">where good health meets real life</p>

  <div class="contact contact--email">
    <svg width="40" height="38" viewBox="0 0 40 38" fill="none" stroke="var(--ink)" stroke-width="2">
      <g transform="rotate(-35 20 20)">
        <rect x="6" y="10" width="28" height="18"/>
        <polyline points="6,10 20,21 34,10"/>
      </g>
    </svg>
    <div class="contact__rule"></div>
    <div class="contact__text">harriet@bramwellpantry-example.com</div>
  </div>

  <div class="contact contact--social">
    <svg width="40" height="38" viewBox="0 0 40 38">
      <rect x="2" y="2" width="36" height="34" rx="4" fill="var(--ink)"/>
    </svg>
    <div class="contact__rule"></div>
    <div class="contact__text">bp_pantry</div>
  </div>

  <div class="contact contact--phone">
    <svg width="40" height="38" viewBox="0 0 40 38" fill="none" stroke="var(--ink)" stroke-width="2">
      <g transform="rotate(-30 20 19)">
        <rect x="12" y="3" width="16" height="32" rx="3"/>
        <line x1="12" y1="8" x2="28" y2="8"/>
        <line x1="12" y1="29" x2="28" y2="29"/>
      </g>
    </svg>
    <div class="contact__rule"></div>
    <div class="contact__text">(555)218-4476</div>
  </div>
</section>

</body>
</html>
```